VELRO - Business cards

Business card to be created for Commercial sales staff

Target Market(s)

Commercial businesses

Industry/Entity Type

Commercial

Contact Information for Business Card

Look professional. For commercial clients

Colors
ffffff

Requirements
Must have
• - Velro Logo
• - Commercial sales staff as postion
• - room for commerical sales manager role
• - person name and their mobile number
• - Website : velropower.com.au
Nice to have
• White background.
• On back of business card just have the logo no other information
Should not have
• Should only have white background on front of card.

```html
<!DOCTYPE html>
<html lang="en">
<head>
<meta charset="utf-8">
<title>Velro – Business Cards</title>
<link rel="stylesheet" href="https://fonts.googleapis.com/css2?family=Quicksand:wght@400;500;700&display=swap">
<style>
  :root {
    --stage: #e6e7ea;
    --card: #ffffff;
    --ink: #2b2e36;
    --accent: #c8161d;
    --muted: #6d7079;
    --line: #9a9ca3;
  }
  * { box-sizing: border-box; margin: 0; padding: 0; }
  html, body { width: 1200px; height: 873px; overflow: hidden; }
  body {
    background: var(--stage);
    font-family: "Quicksand", sans-serif;
    color: var(--ink);
    position: relative;
  }
  .card {
    position: absolute;
    top: 286px;
    width: 520px;
    height: 300px;
    background: var(--card);
    border-radius: 6px;
    box-shadow: 0 10px 28px rgba(0,0,0,.18);
    overflow: hidden;
  }
  .card--front { left: 50px; }
  .card--back { left: 630px; }
  .card__tabs { position: absolute; inset: 0; width: 100%; height: 100%; }
  .tab { fill: var(--ink); }

  .wordmark {
    position: absolute;
    display: flex;
    align-items: center;
    gap: 10px;
    font-weight: 700;
    color: var(--ink);
    letter-spacing: 2px;
    line-height: 1;
  }
  .wordmark__dot {
    display: block;
    border-radius: 50%;
    background: var(--accent);
  }
  .card--front .wordmark { left: 38px; top: 126px; font-size: 44px; }
  .card--front .wordmark__dot { width: 16px; height: 16px; }
  .card--back .wordmark { left: 0; right: 0; top: 112px; justify-content: center; font-size: 68px; }
  .card--back .wordmark__dot { width: 22px; height: 22px; }

  .divider { position: absolute; left: 0; top: 0; width: 100%; height: 100%; }
  .divider line { stroke: var(--accent); stroke-width: 1.4; }

  .contact { position: absolute; left: 268px; top: 58px; }
  .contact__name {
    font-size: 30px;
    font-weight: 700;
    color: var(--accent);
    line-height: 1.05;
  }
  .contact__role {
    font-size: 16px;
    color: var(--muted);
    margin-top: 2px;
  }
  .contact__list { list-style: none; margin-top: 22px; }
  .contact__item {
    display: flex;
    align-items: center;
    gap: 10px;
    font-size: 15px;
    color: var(--muted);
    margin-bottom: 11px;
  }
  .contact__icon { width: 20px; height: 20px; flex: none; }
  .contact__icon circle.ring { fill: none; stroke: var(--muted); stroke-width: 1.3; }
  .contact__icon .glyph { fill: none; stroke: var(--muted); stroke-width: 1.2; }
</style>
</head>
<body>

  <section class="card card--front" aria-label="Business card front">
    <svg class="card__tabs" viewBox="0 0 520 300" aria-hidden="true">
      <path class="tab" d="M0 0 H170 Q178 0 178 6 Q178 10 170 10 H0 Z"/>
      <path class="tab" d="M520 300 H350 Q342 300 342 294 Q342 290 350 290 H520 Z"/>
    </svg>

    <div class="wordmark"><span class="wordmark__dot"></span>VELRO</div>

    <svg class="divider" viewBox="0 0 520 300" aria-hidden="true">
      <line x1="236" y1="262" x2="252" y2="40"/>
    </svg>

    <div class="contact">
      <h1 class="contact__name">Your Name</h1>
      <p class="contact__role">Position</p>
      <ul class="contact__list">
        <li class="contact__item">
          <svg class="contact__icon" viewBox="0 0 20 20" aria-hidden="true">
            <circle class="ring" cx="10" cy="10" r="9"/>
            <rect class="glyph" x="7" y="5" width="6" height="10" rx="1"/>
          </svg>
          555-010-200
        </li>
        <li class="contact__item">
          <svg class="contact__icon" viewBox="0 0 20 20" aria-hidden="true">
            <circle class="ring" cx="10" cy="10" r="9"/>
            <rect class="glyph" x="5.5" y="6.5" width="9" height="7"/>
            <path class="glyph" d="M5.5 6.5 L10 10.5 L14.5 6.5"/>
          </svg>
          name@velropower.com.au
        </li>
        <li class="contact__item">
          <svg class="contact__icon" viewBox="0 0 20 20" aria-hidden="true">
            <circle class="ring" cx="10" cy="10" r="9"/>
            <circle class="glyph" cx="10" cy="10" r="5"/>
            <path class="glyph" d="M5 10 H15 M10 5 Q7 10 10 15 M10 5 Q13 10 10 15"/>
          </svg>
          velropower.com.au
        </li>
      </ul>
    </div>
  </section>

  <section class="card card--back" aria-label="Business card back">
    <svg class="card__tabs" viewBox="0 0 520 300" aria-hidden="true">
      <path class="tab" d="M0 0 H170 Q178 0 178 6 Q178 10 170 10 H0 Z"/>
      <path class="tab" d="M520 300 H350 Q342 300 342 294 Q342 290 350 290 H520 Z"/>
    </svg>
    <div class="wordmark"><span class="wordmark__dot"></span>VELRO</div>
  </section>

</body>
</html>
```